BRM Going Cashless

Hello,
We are a medical office looking to get a flyer created to promote to our patients we will be going "Cashless." Our tagline will be "Cash-Less is Stress-Less"

"Starting in July, to offer you the fastest and most convenient service, we are transitioning to a cashless system. You can now enjoy faster checkout times and greater security with card and contactless payments. More info to come."

I've added two other flyers as sample designs we've used.

Please include logo, addresses, website, phone number

Files to include jpeg, png, pdf (under 5mb), Facebook and Instagram sizing.

Thank you,
Marlo

```html
<!DOCTYPE html>
<html lang="en">
<head>
<meta charset="utf-8">
<title>BRM Foot &amp; Ankle – Cash-Less Is Stress-Less</title>
<link rel="stylesheet" href="https://fonts.googleapis.com/css2?family=Bebas+Neue&family=Montserrat:wght@400;500;600;700;800&family=Sacramento&display=swap">
<style>
:root{
  --board:#c6c6c6;
  --ink:#2d2d2d;
  --teal:#55c1a6;
  --orange:#f07a45;
  --white:#ffffff;
  --label:#3a3a3a;
  --line:#8a8a8a;
}
*{margin:0;padding:0;box-sizing:border-box}
html,body{width:1200px;height:2548px;overflow:hidden;background:var(--board)}
body{position:relative;font-family:"Montserrat",Arial,sans-serif;color:var(--white)}
.artboard{position:absolute;overflow:hidden;background:var(--ink);box-shadow:14px 16px 18px rgba(0,0,0,.28)}
.size-label{position:absolute;left:0;width:1200px;text-align:center;font-family:"Montserrat",Arial,sans-serif;font-weight:500;font-size:27px;color:var(--label)}
.abs{position:absolute}
.bg-shape{position:absolute;left:0;top:0}
.script{font-family:"Sacramento",cursive;-webkit-text-stroke:2.5px currentColor;line-height:1;white-space:nowrap}
.headline{font-family:"Bebas Neue",Impact,sans-serif;line-height:1;white-space:nowrap}
.badge{position:absolute;background:var(--orange);color:var(--white);border:2px solid var(--white);border-radius:8px;font-weight:600;letter-spacing:.22em;text-align:center;box-shadow:0 0 0 2px var(--orange)}
.month{font-weight:800;line-height:1;white-space:nowrap}
.body-copy{color:var(--ink);font-weight:500;line-height:1.22}
.product-visual{position:absolute;border-radius:30px;background:radial-gradient(ellipse at 45% 55%,#3a4c66 0%,#1f2a3a 55%,rgba(30,40,55,0) 78%)}
.spaced{letter-spacing:.38em;font-weight:700;white-space:nowrap}
.brand{position:absolute;display:flex;align-items:center;gap:10px;color:var(--orange);font-weight:800;white-space:nowrap}
.brand .dot{border-radius:50%;background:var(--teal);flex:none}
.brand .name{line-height:1.05}
.office h4{color:var(--teal);font-weight:700}
.office p{color:var(--white)}
.web{position:absolute;background:var(--orange);color:var(--white);border:2px solid var(--white);white-space:nowrap;letter-spacing:.18em}
.web b{font-weight:800}
/* square post */
.post{left:265px;top:141px;width:669px;height:744px}
.post .office{position:absolute;top:618px;text-align:center;font-size:8.5px;line-height:1.3}
.post .office h4{font-size:11px;margin:4px 0 3px}
/* tall post */
.story{left:237px;top:1058px;width:733px;height:1303px}
.story .office{position:absolute;top:1098px;width:217px;height:115px;text-align:center}
.story .office .box{position:absolute;left:0;top:10px;width:217px;height:115px;background:var(--ink);border-radius:4px}
.story .office .inner{position:relative;padding-top:24px}
.story .office h4{font-size:20px;margin-bottom:6px}
.story .office p{font-size:14.5px;line-height:1.22}
.bullets{list-style:none}
.bullets li{display:flex;align-items:center;gap:10px;color:var(--ink);font-size:21.5px;font-weight:500;height:35px}
.bullets li::before{content:"";width:14px;height:14px;border-radius:50%;background:var(--orange);flex:none}
</style>
</head>
<body>

<!-- Square feed post -->
<section class="artboard post">
  <svg class="bg-shape" width="669" height="744" viewBox="0 0 669 744">
    <path d="M0 0 H495 C470 150 520 330 330 420 C220 460 100 445 0 425 Z" fill="var(--teal)"/>
  </svg>

  <div class="product-visual" role="img" aria-label="Card payment terminal with two floating bank cards and a smartphone showing a payment successful tick" style="left:370px;top:115px;width:295px;height:350px"></div>

  <div class="abs script" style="left:24px;top:52px;font-size:92px;color:var(--ink)">Cash-Less</div>
  <div class="abs headline" style="left:32px;top:148px;font-size:72px;color:var(--white)">IS STRESS-LESS</div>

  <div class="badge" style="left:35px;top:240px;width:162px;height:30px;font-size:21px;line-height:26px">STARTING</div>
  <div class="abs month" style="left:34px;top:280px;font-size:56px;color:var(--white)">IN JULY</div>
  <p class="abs body-copy" style="left:35px;top:345px;width:250px;font-size:14.5px">To offer you the fastest and most convenient service, we are transitioning to a cashless system</p>

  <p class="abs" style="left:37px;top:466px;font-size:18px;color:var(--white)">Now you can enjoy</p>
  <p class="abs" style="left:37px;top:488px;width:300px;font-size:18.5px;font-weight:700;color:var(--teal);line-height:1.25">faster checkout times and greater security with card and</p>
  <p class="abs" style="left:37px;top:536px;font-size:27px;font-weight:800;font-style:italic;color:var(--orange);white-space:nowrap">CONTACTLESS PAYMENTS</p>
  <p class="abs spaced" style="left:38px;top:586px;font-size:11px;color:var(--white)">MORE INFO TO COME....</p>

  <div class="brand" style="left:440px;top:535px;font-size:20px">
    <span class="dot" style="width:28px;height:28px"></span><span class="name">BRM<br>FOOT &amp; ANKLE</span>
  </div>

  <svg class="abs" style="left:36px;top:603px" width="600" height="2"><rect width="600" height="1" fill="var(--line)"/></svg>
  <svg class="abs" style="left:141px;top:615px" width="2" height="80"><line x1="1" y1="0" x2="1" y2="80" stroke="var(--line)" stroke-dasharray="3 3"/></svg>
  <svg class="abs" style="left:281px;top:615px" width="2" height="80"><line x1="1" y1="0" x2="1" y2="80" stroke="var(--line)" stroke-dasharray="3 3"/></svg>

  <div class="office" style="left:36px;width:104px">
    <svg width="16" height="16" viewBox="0 0 16 16"><circle cx="8" cy="8" r="8" fill="var(--orange)"/><path d="M8 3.5a3 3 0 0 0-3 3c0 2.2 3 5.5 3 5.5s3-3.3 3-5.5a3 3 0 0 0-3-3z" fill="var(--white)"/><circle cx="8" cy="6.5" r="1.1" fill="var(--orange)"/></svg>
    <h4>Frederick Office</h4>
    <p>27 Linden Park Dr. Suite110 Frederick, MD21701</p>
  </div>
  <div class="office" style="left:148px;width:132px">
    <svg width="16" height="16" viewBox="0 0 16 16"><circle cx="8" cy="8" r="8" fill="var(--orange)"/><path d="M8 3.5a3 3 0 0 0-3 3c0 2.2 3 5.5 3 5.5s3-3.3 3-5.5a3 3 0 0 0-3-3z" fill="var(--white)"/><circle cx="8" cy="6.5" r="1.1" fill="var(--orange)"/></svg>
    <h4>Martinsburg Office</h4>
    <p>48 Orchard View Rd.<br>Martinsburg,WV25404</p>
  </div>
  <div class="office" style="left:287px;width:100px">
    <svg width="16" height="16" viewBox="0 0 16 16"><circle cx="8" cy="8" r="8" fill="var(--orange)"/><path d="M8 3.5a3 3 0 0 0-3 3c0 2.2 3 5.5 3 5.5s3-3.3 3-5.5a3 3 0 0 0-3-3z" fill="var(--white)"/><circle cx="8" cy="6.5" r="1.1" fill="var(--orange)"/></svg>
    <h4>Urbana Office</h4>
    <p>912 Meadow Gate Blvd.Suite 205 Urbana, MD21704</p>
  </div>

  <p class="abs spaced" style="left:436px;top:620px;font-size:13px;color:var(--teal);letter-spacing:.28em">CONTACT US TODAY</p>
  <svg class="abs" style="left:435px;top:645px" width="26" height="26" viewBox="0 0 26 26"><circle cx="13" cy="13" r="13" fill="var(--orange)"/><path d="M9 7.5l2.2-.4 1.2 3-1.5 1.1a8 8 0 0 0 3.2 3.2l1.1-1.5 3 1.2-.4 2.2c-.2.7-.9 1-1.6.9C11.5 16.4 9.6 14.5 8.8 9.1c-.1-.7.2-1.4.2-1.6z" fill="var(--white)"/></svg>
  <p class="abs" style="left:467px;top:641px;font-size:26px;font-weight:700;color:var(--white)">(555)014-0192</p>
  <div class="web" style="left:432px;top:680px;width:245px;height:24px;font-size:13px;line-height:20px;padding-left:12px;border-right:none">www.<b>brmfootcare</b>.com</div>
</section>
<p class="size-label" style="top:945px">1080 X 1080</p>

<!-- Tall story post -->
<section class="artboard story">
  <svg class="bg-shape" width="733" height="1303" viewBox="0 0 733 1303">
    <path d="M0 715 Q366 545 733 715 V1303 H0 Z" fill="var(--teal)"/>
  </svg>

  <div class="product-visual" role="img" aria-label="Card payment terminal with two floating bank cards and a smartphone showing a payment successful tick" style="left:85px;top:425px;width:560px;height:445px"></div>

  <div class="brand" style="left:0;width:733px;justify-content:center;top:55px;font-size:30px">
    <span class="dot" style="width:34px;height:34px"></span><span class="name">BRM FOOT &amp; ANKLE</span>
  </div>

  <div class="abs script" style="left:0;width:733px;text-align:center;top:150px;font-size:150px;color:var(--teal)">Cash-Less</div>
  <div class="abs headline" style="left:0;width:733px;text-align:center;top:290px;font-size:124px;color:var(--orange)">IS STRESS-LESS</div>

  <div class="badge" style="left:39px;top:877px;width:208px;height:36px;font-size:27px;line-height:32px">STARTING</div>
  <div class="abs month" style="left:35px;top:922px;font-size:66px;color:var(--white)">IN JULY</div>
  <p class="abs body-copy" style="left:36px;top:1003px;width:320px;font-size:18.5px">To offer you the fastest and most convenient service, we are transitioning to a cashless system</p>

  <svg class="abs" style="left:365px;top:875px" width="2" height="200"><line x1="1" y1="0" x2="1" y2="200" stroke="var(--ink)" stroke-width="1" stroke-dasharray="4 3"/></svg>

  <p class="abs" style="left:393px;top:878px;font-size:27px;font-weight:700;white-space:nowrap"><span style="color:var(--white)">YOU CAN </span><span style="color:var(--orange)">NOW ENJOY</span></p>
  <ul class="abs bullets" style="left:396px;top:925px">
    <li>Faster checkout times</li>
    <li>Greater security with card</li>
    <li>Contactless payments</li>
  </ul>
  <p class="abs spaced" style="left:398px;top:1057px;font-size:14px;color:var(--white)">MORE INFO TO COME....</p>

  <div class="office" style="left:37px">
    <div class="box"></div>
    <svg class="abs" style="left:96px;top:0" width="26" height="26" viewBox="0 0 16 16"><circle cx="8" cy="8" r="8" fill="var(--orange)"/><path d="M8 3.5a3 3 0 0 0-3 3c0 2.2 3 5.5 3 5.5s3-3.3 3-5.5a3 3 0 0 0-3-3z" fill="var(--white)"/><circle cx="8" cy="6.5" r="1.1" fill="var(--orange)"/></svg>
    <div class="inner"><h4>Frederick Office</h4><p>27 Linden Park<br>Dr.Suite110 Frederick,<br>MD21701</p></div>
  </div>
  <div class="office" style="left:262px">
    <div class="box"></div>
    <svg class="abs" style="left:96px;top:0" width="26" height="26" viewBox="0 0 16 16"><circle cx="8" cy="8" r="8" fill="var(--orange)"/><path d="M8 3.5a3 3 0 0 0-3 3c0 2.2 3 5.5 3 5.5s3-3.3 3-5.5a3 3 0 0 0-3-3z" fill="var(--white)"/><circle cx="8" cy="6.5" r="1.1" fill="var(--orange)"/></svg>
    <div class="inner"><h4>Martinsburg Office</h4><p>48 Orchard View Rd.<br>Martinsburg,WV25404</p></div>
  </div>
  <div class="office" style="left:488px">
    <div class="box"></div>
    <svg class="abs" style="left:96px;top:0" width="26" height="26" viewBox="0 0 16 16"><circle cx="8" cy="8" r="8" fill="var(--orange)"/><path d="M8 3.5a3 3 0 0 0-3 3c0 2.2 3 5.5 3 5.5s3-3.3 3-5.5a3 3 0 0 0-3-3z" fill="var(--white)"/><circle cx="8" cy="6.5" r="1.1" fill="var(--orange)"/></svg>
    <div class="inner"><h4>Urbana Office</h4><p>912 Meadow Gate<br>Blvd.Suite 205 Urbana,<br>MD21704</p></div>
  </div>

  <svg class="abs" style="left:38px;top:1240px" width="40" height="40" viewBox="0 0 26 26"><circle cx="13" cy="13" r="13" fill="var(--orange)"/><path d="M9 7.5l2.2-.4 1.2 3-1.5 1.1a8 8 0 0 0 3.2 3.2l1.1-1.5 3 1.2-.4 2.2c-.2.7-.9 1-1.6.9C11.5 16.4 9.6 14.5 8.8 9.1c-.1-.7.2-1.4.2-1.6z" fill="var(--white)"/></svg>
  <p class="abs" style="left:88px;top:1234px;font-size:36px;font-weight:700;color:var(--ink);white-space:nowrap">(555)014-0192</p>
  <div class="web" style="left:378px;top:1236px;width:360px;height:38px;border-radius:19px 0 0 19px;font-size:20px;line-height:34px;padding-left:20px;border-right:none">www.<b>brmfootcare</b>.com</div>
</section>
<p class="size-label" style="top:2435px">1920 X 1080</p>

</body>
</html>
```